Martin Hale PA Card Logo

Current logo attached. Its 25 year old logo I have used. Looking for a new fresh elegant professional look/design for a law firm that has high net worth clientele and is estate planning business law firm. Firm mis in Palm Beach Florida.
One sided card linen stock white will be used. Logo section name section. Logo should include nice elegant design using the letter "M" perhapa (I am not wed to current font of the M on current logo.) Be creative there with logo design. My initials are MH.......color scheme I figure 3 tone... Raised Gold Foil, Blue name of firm = Martin Hale, P.A. My practice focus is Family and Business Asset Protection. My name is Martin M. Hale, Esq. Practice specialties include Asset Protection trusts, Business Succession Planning, LLC law, Estate Planning, Medicaid Planning (Maybe put those topics in bullets in a section of card. Bottom of card can be reserved smaller print address phone website and email address. Address section is not as important as logo and topics of practice on front. I foresee address section can be in dark blue. MY name and Topics dark blue as well.
Target Market(s)
affluent; business owners executives; wealth 2-10 million net worth
Industry/Entity Type
business law and estate planning
Contact Information for Business Card
White thick linen one sided

```html
<!DOCTYPE html>
<html lang="en">
<head>
<meta charset="UTF-8">
<title>Martin Hale, P.A. — Business Card</title>
<link rel="stylesheet" href="https://fonts.googleapis.com/css2?family=Cinzel:wght@400;500&family=EB+Garamond:wght@400&family=Arimo:wght@400&display=swap">
<style>
  :root {
    --backdrop: #2e2e30;
    --card: #ffffff;
    --navy: #1f3a68;
    --gold: #c98a2a;
    --gold-soft: #d9a552;
  }
  * { box-sizing: border-box; margin: 0; padding: 0; }
  html, body { width: 1200px; height: 800px; overflow: hidden; }
  body { background: var(--backdrop); position: relative; }

  .card {
    position: absolute; left: 100px; top: 114px;
    width: 1000px; height: 572px;
    background: var(--card); border-radius: 34px;
    overflow: hidden;
  }

  /* Brand block */
  .brand { position: absolute; left: 70px; top: 92px; display: flex; align-items: center; gap: 22px; }
  .brand-mark { width: 64px; height: 64px; border-radius: 50%; background: var(--gold); flex: none; }
  .brand-text { width: 420px; }
  .brand-name {
    font-family: "Cinzel", serif; font-weight: 500; color: var(--navy);
    font-size: 38px; letter-spacing: 1px; line-height: 1.1; white-space: nowrap;
  }
  .brand-rule { height: 3px; background: var(--gold); margin: 6px 0 8px -90px; width: 520px; }
  .brand-tagline {
    font-family: "Cinzel", serif; color: var(--navy);
    font-size: 24px; letter-spacing: 1.5px; padding-left: 58px; white-space: nowrap;
  }

  /* Practice areas */
  .practice-list {
    position: absolute; left: 620px; top: 96px; list-style: none;
    font-family: "EB Garamond", serif; color: var(--navy); font-size: 27px; line-height: 1.32;
  }
  .practice-list li { position: relative; padding-left: 22px; }
  .practice-list li::before {
    content: ""; position: absolute; left: 0; top: 14px;
    width: 8px; height: 8px; border-radius: 50%; background: var(--gold);
  }

  /* Attorney identity */
  .attorney { position: absolute; left: 118px; top: 280px; }
  .attorney-name {
    font-family: "Cinzel", serif; color: var(--navy); font-size: 34px; letter-spacing: 1px; white-space: nowrap;
  }
  .attorney-title {
    font-family: "Cinzel", serif; color: var(--gold); font-size: 22px; letter-spacing: 1.5px; margin-top: 2px;
  }
  .edge-tab {
    position: absolute; left: -12px; top: 344px; width: 44px; height: 42px;
    background: var(--gold); border-radius: 8px;
  }

  /* Contact */
  .contact-list {
    position: absolute; left: 118px; top: 372px; list-style: none;
    font-family: "Arimo", sans-serif; color: var(--navy); font-size: 23px; line-height: 1;
  }
  .contact-list li { display: flex; align-items: center; gap: 16px; height: 36px; }
  .contact-icon { width: 24px; height: 24px; flex: none; }

  /* Divider + address */
  .divider { position: absolute; height: 2px; background: var(--gold); }
  .divider-main { left: 440px; top: 408px; width: 500px; }
  .divider-base { left: 118px; top: 528px; width: 822px; }
  .address {
    position: absolute; left: 446px; top: 440px; display: flex; align-items: center; gap: 10px;
    font-family: "Arimo", sans-serif; color: var(--navy); font-size: 25px; white-space: nowrap;
  }
  .address-pin { width: 18px; height: 24px; }
</style>
</head>
<body>
  <main class="card">
    <header class="brand">
      <span class="brand-mark" aria-hidden="true"></span>
      <div class="brand-text">
        <div class="brand-name">Martin Hale, P.A.</div>
        <div class="brand-rule"></div>
        <div class="brand-tagline">Elder Law Attorney</div>
      </div>
    </header>

    <ul class="practice-list">
      <li>Asset Protection trusts</li>
      <li>Business Succession Planning</li>
      <li>LLC law</li>
      <li>Estate Planning</li>
      <li>Medicaid Planning</li>
    </ul>

    <div class="edge-tab" aria-hidden="true"></div>
    <section class="attorney">
      <div class="attorney-name">Martin Hale, P.A.</div>
      <div class="attorney-title">Law Attorney</div>
    </section>

    <ul class="contact-list">
      <li>
        <svg class="contact-icon" viewBox="0 0 24 24" aria-hidden="true">
          <rect width="24" height="24" rx="3" fill="#c98a2a"/>
          <rect x="7" y="4" width="10" height="16" rx="2" fill="none" stroke="#fff" stroke-width="1.8"/>
          <line x1="10" y1="17" x2="14" y2="17" stroke="#fff" stroke-width="1.6"/>
        </svg>
        <span>044-555 210 384</span>
      </li>
      <li>
        <svg class="contact-icon" viewBox="0 0 24 24" aria-hidden="true">
          <rect width="24" height="24" rx="3" fill="#c98a2a"/>
          <path d="M5 12 L19 5 L14 19 L11.5 13.5 Z" fill="#fff"/>
        </svg>
        <span>office@halelawpa.com</span>
      </li>
      <li>
        <svg class="contact-icon" viewBox="0 0 24 24" aria-hidden="true">
          <rect width="24" height="24" rx="3" fill="#c98a2a"/>
          <circle cx="12" cy="12" r="7" fill="none" stroke="#fff" stroke-width="1.6"/>
          <ellipse cx="12" cy="12" rx="3" ry="7" fill="none" stroke="#fff" stroke-width="1.3"/>
          <line x1="5" y1="12" x2="19" y2="12" stroke="#fff" stroke-width="1.3"/>
        </svg>
        <span>www.halelawpa.com</span>
      </li>
    </ul>

    <div class="divider divider-main"></div>
    <div class="address">
      <svg class="address-pin" viewBox="0 0 18 24" aria-hidden="true">
        <path d="M9 1 C4.5 1 1.5 4.3 1.5 8.5 C1.5 14 9 23 9 23 C9 23 16.5 14 16.5 8.5 C16.5 4.3 13.5 1 9 1 Z" fill="#c98a2a"/>
        <circle cx="9" cy="8.5" r="3" fill="#fff"/>
      </svg>
      <span>4410 Harbor Palm Blvd, 210-B, FL 33480</span>
    </div>
    <div class="divider divider-base"></div>
  </main>
</body>
</html>
```